Bright Canyon, LLC Business Card Design

We need a product business card designed for a new company Bright Canyon, LLC. We make and resell waterless RV cleaner, polish and protectant. It cleans and protects in a simple spray and wipe step leaving the surface protected and conditioned to repel dust, dirt, water, smudges, bugs and fingerprints while preventing fogging. Safe on acrylic, clarisheet, durvane, plastic, rubber, painted surfaces, chrome, stainless, aluminum, vinyl, leather, glass.... This is an eco-friendly green product.

We want to play off the company name to tell the consumer that the product is easy to use and associate to the nostalgics 1950's in the USA... Thinking old travel trailer with hot rod truck pulling it as the graphic, maybe the husband cleaning the truck and the wife cleaning the trailer for a Bright Canyon surface.
Updates

Just posted our newly finished logo. Need to have "Cleaner and Protectant" added to the design as well. Thanks everyone that has submitted thus far, i am working to get comments on all.

If you need a different file format, please let me know. Thank you.

Most important info, is the logo, website and the words "Cleaner" or "Clean" along "Protectant" or "Protect" the remainder is of less importance. Highlight: www.brightcanyoncleaner.example Focus is on company brand for Brighter Canyon Cleaner product: However, need a section for the following contact info: John Doe (xxx) xxx-xxxx email address Would like space for QR Code if possible.

Target Market(s)

Adults in the USA between ages of 35-75 that are actively involved in the Recreational Vehicle (RV), travel trailer, and hot rod lifestyle. We are targeting the RV marked of the high end travel, 5th wheel and bus RV market. Along with hot rods, automotive and motorcycle market.

Industry/Entity Type

Travel

Requirements
Must have
• Most important info, is the logo, website and the words "Cleaner" or "Clean" along "Protectant" or "Protect" the remainder is of less importance.

Highlight:
www.brightcanyoncleaner.example

Focus is on company brand for Brighter Canyon Cleaner product: However, need a section for the following contact info:

John Doe
(xxx) xxx-xxxx
email address
Nice to have
• Would like a space for a QR Code.

```html
<!DOCTYPE html>
<html lang="en">
<head>
<meta charset="UTF-8">
<title>Bright Canyon, LLC — Business Card</title>
<link rel="stylesheet" href="https://fonts.googleapis.com/css2?family=Baloo+2:wght@800&family=Exo+2:wght@400;500;600&display=swap">
<style>
  :root {
    --orange: #f05a38;
    --silver-light: #ffffff;
    --silver-mid: #ececec;
    --silver-dark: #cfcfcf;
    --ink: #4a4a4a;
    --ink-soft: #5c5c5c;
    --white: #ffffff;
    --trim: rgba(255,255,255,0.55);
    --backdrop: #e6e4e1;
  }
  * { box-sizing: border-box; margin: 0; padding: 0; }
  html, body {
    width: 1200px;
    height: 906px;
    overflow: hidden;
    background: var(--backdrop);
    font-family: "Exo 2", Arial, sans-serif;
  }
  .stage { position: relative; width: 1200px; height: 906px; }

  .card {
    position: absolute;
    width: 740px;
    height: 410px;
    overflow: hidden;
    box-shadow: 0 10px 28px rgba(0,0,0,0.18);
    background: var(--orange);
  }
  .card--front { left: 150px; top: 34px; }
  .card--back  { left: 310px; top: 466px; }

  .silver-band {
    position: absolute;
    left: 0; right: 0; top: 0;
    background: linear-gradient(100deg, var(--silver-dark) 0%, var(--silver-light) 45%, var(--silver-mid) 75%, var(--silver-dark) 100%);
  }
  .card--front .silver-band { height: 250px; }
  .card--back  .silver-band { height: 200px; }

  /* chrome trim stripes along the band edge, travel-trailer style */
  .trim {
    position: absolute;
    left: 0; right: 0;
    height: 10px;
    border-top: 2px solid var(--trim);
    border-bottom: 2px solid var(--trim);
  }
  .card--front .trim { top: 258px; }
  .card--back  .trim { top: 208px; }

  .brand {
    position: absolute;
    line-height: 1;
  }
  .brand-name {
    font-family: "Baloo 2", "Arial Black", sans-serif;
    font-weight: 800;
    font-size: 50px;
    letter-spacing: 1px;
    color: var(--ink);
    text-transform: uppercase;
  }
  .tagline {
    font-weight: 600;
    font-size: 17px;
    letter-spacing: 5px;
    text-transform: uppercase;
    color: var(--orange);
    margin-top: 8px;
  }
  .card--front .brand { left: 0; right: 0; top: 86px; text-align: center; }
  .card--back  .brand { left: 40px; top: 112px; }
  .card--back  .brand-name { font-size: 40px; }
  .card--back  .tagline { font-size: 13px; letter-spacing: 4px; margin-top: 6px; }

  .qr-space {
    position: absolute;
    left: 40px;
    bottom: 24px;
    width: 104px;
    height: 104px;
    background: var(--white);
    border: 3px dashed var(--orange);
    outline: 4px solid var(--white);
  }

  .website {
    position: absolute;
    right: 44px;
    bottom: 46px;
    color: var(--white);
    font-size: 22px;
    letter-spacing: 1px;
  }

  .person {
    position: absolute;
    right: 40px;
    top: 46px;
    text-align: right;
    color: var(--ink);
  }
  .person__name {
    font-size: 30px;
    letter-spacing: 2px;
    text-transform: uppercase;
  }
  .person__title {
    font-size: 13px;
    letter-spacing: 2px;
    text-transform: uppercase;
    color: var(--ink-soft);
    margin-top: 2px;
  }

  .contact-row {
    position: absolute;
    left: 0; right: 0; top: 222px; bottom: 0;
    display: flex;
    justify-content: space-around;
    align-items: center;
    padding: 0 20px;
  }
  .contact {
    display: flex;
    flex-direction: column;
    align-items: center;
    gap: 14px;
    color: var(--white);
    font-size: 16px;
    line-height: 1.35;
    text-align: center;
    letter-spacing: 0.5px;
  }
  .contact__icon {
    width: 56px;
    height: 56px;
    border-radius: 50%;
    background: var(--white);
    display: flex;
    align-items: center;
    justify-content: center;
  }
  .contact__icon svg { width: 30px; height: 30px; }
</style>
</head>
<body>
<main class="stage">

  <section class="card card--front" aria-label="Business card front">
    <div class="silver-band"></div>
    <div class="brand">
      <div class="brand-name">Bright Canyon</div>
      <div class="tagline">Cleaner &amp; Protectant</div>
    </div>
    <div class="trim"></div>
    <div class="qr-space" role="img" aria-label="Space reserved for QR code"></div>
    <div class="website">www.brightcanyoncleaner.example</div>
  </section>

  <section class="card card--back" aria-label="Business card back">
    <div class="silver-band"></div>
    <div class="brand">
      <div class="brand-name">Bright Canyon</div>
      <div class="tagline">Cleaner &amp; Protectant</div>
    </div>
    <div class="person">
      <div class="person__name">Jonathan Dale</div>
      <div class="person__title">General Manager</div>
    </div>
    <div class="trim"></div>

    <div class="contact-row">
      <div class="contact contact--address">
        <span class="contact__icon">
          <svg viewBox="0 0 24 24" fill="none" stroke="#f05a38" stroke-width="2.4" stroke-linejoin="round">
            <path d="M3 12 L12 4 L21 12"/>
            <path d="M6 10 V20 H18 V10"/>
            <rect x="10" y="14" width="4" height="6" fill="#f05a38" stroke="none"/>
          </svg>
        </span>
        <span>204, 9th Floor, Mesa Plaza<br>Canyon View Road</span>
      </div>

      <div class="contact contact--phone">
        <span class="contact__icon">
          <svg viewBox="0 0 24 24" fill="#f05a38">
            <path d="M3 8 C3 5 7 4 12 4 C17 4 21 5 21 8 V10 H16 V8 H8 V10 H3 Z"/>
            <path d="M7 11 H17 L20 19 H4 Z"/>
            <circle cx="12" cy="15" r="2.2" fill="#ffffff"/>
          </svg>
        </span>
        <span>012 555 0147<br>012 555 0148</span>
      </div>

      <div class="contact contact--web">
        <span class="contact__icon">
          <svg viewBox="0 0 24 24" fill="none" stroke="#f05a38" stroke-width="1.8">
            <circle cx="12" cy="12" r="9"/>
            <ellipse cx="12" cy="12" rx="4" ry="9"/>
            <line x1="3" y1="12" x2="21" y2="12"/>
            <path d="M5 7 H19 M5 17 H19"/>
          </svg>
        </span>
        <span>jonathan@brightcanyon.example<br>www.brightcanyoncleaner.example</span>
      </div>
    </div>
  </section>

</main>
</body>
</html>
```